tovrin company need business card, envelope and letterhead design

Check on the attached file wherein you can find our logo and information about the company
Business card will double sided English version and Arabic version

Industry/Entity Type

Business

Requirements
Must have
• include the design also for the letterhead and envelop
Nice to have

```html
<!DOCTYPE html>
<html lang="en">
<head>
<meta charset="utf-8">
<title>Tovrin Envelope</title>
<link rel="stylesheet" href="https://fonts.googleapis.com/css2?family=Poppins:wght@600;700&display=swap">
<style>
  :root {
    --stage: #383838;
    --paper: #ffffff;
    --brand-blue: #1a75bb;
    --brand-gray: #808285;
    --text-gray: #6d6e71;
    --ghost: #eef1f8;
  }
  * { margin: 0; padding: 0; box-sizing: border-box; }
  html, body { width: 1171px; height: 1200px; overflow: hidden; }
  body { background: var(--stage); position: relative; font-family: "Poppins", Arial, sans-serif; }

  .envelope {
    position: absolute; left: 119px; width: 933px; height: 405px;
    background: var(--paper); overflow: hidden;
    box-shadow: 6px 8px 10px rgba(0,0,0,0.55);
  }
  .envelope--front { top: 159px; }
  .envelope--back { top: 634px; }

  .edge-tab { position: absolute; left: 0; top: 69px; width: 7px; height: 58px; background: var(--brand-blue); }

  .brand { position: absolute; display: flex; align-items: center; gap: 10px; font-weight: 700; letter-spacing: 1.5px; line-height: 1; }
  .brand__mark { width: 34px; height: 34px; background: currentColor; }
  .brand--front { left: 61px; top: 77px; color: var(--brand-blue); font-size: 38px; }
  .brand--flap { left: 376px; top: 52px; color: var(--paper); font-size: 26px; gap: 7px; }
  .brand--flap .brand__mark { width: 22px; height: 22px; }

  .ghost-mark { position: absolute; background: var(--ghost); }
  .ghost-mark--front { left: 554px; top: 27px; width: 347px; height: 347px; }
  .ghost-mark--back { left: 27px; top: 156px; width: 217px; height: 217px; }

  .contact { position: absolute; top: 313px; left: 54px; display: flex; align-items: center; }
  .contact__address { font-size: 9px; font-weight: 700; color: var(--brand-blue); line-height: 15px; padding-right: 9px; }
  .contact__divider { width: 1px; height: 41px; background: var(--brand-gray); }
  .contact__lines { padding-left: 8px; font-size: 8px; font-weight: 600; color: var(--text-gray); line-height: 15px; }
  .contact__line { display: flex; align-items: center; gap: 5px; }
  .contact__icon { width: 10px; height: 10px; }

  .footer-band { position: absolute; left: 0; bottom: 0; width: 933px; height: 15px; }
  .flap { position: absolute; left: 0; top: 0; width: 933px; height: 132px; }
</style>
</head>
<body>

<section class="envelope envelope--front" aria-label="Envelope front">
  <div class="edge-tab"></div>
  <div class="brand brand--front"><span class="brand__mark"></span>TOVRIN</div>
  <div class="ghost-mark ghost-mark--front"></div>

  <div class="contact">
    <div class="contact__address">
      <p>Cedar Grove Road</p>
      <p>North District - P.O. Box 4410-22815</p>
    </div>
    <div class="contact__divider"></div>
    <div class="contact__lines">
      <p class="contact__line">
        <svg class="contact__icon" viewBox="0 0 10 10"><circle cx="5" cy="5" r="5" fill="#1a75bb"/><path d="M3.4 2.6l1 1-.5.7a3.5 3.5 0 0 0 1.8 1.8l.7-.5 1 1-.6.8C4.8 7.3 2.7 5.2 2.6 3.2z" fill="#fff"/></svg>
        +966 555 318 204
      </p>
      <p class="contact__line">
        <svg class="contact__icon" viewBox="0 0 10 10"><circle cx="5" cy="5" r="5" fill="#1a75bb"/><rect x="2.5" y="3.2" width="5" height="3.6" fill="none" stroke="#fff" stroke-width=".8"/><path d="M2.5 3.3L5 5.2l2.5-1.9" fill="none" stroke="#fff" stroke-width=".8"/></svg>
        tovrin.sa@mailbox.com
      </p>
    </div>
  </div>

  <svg class="footer-band" viewBox="0 0 933 15" preserveAspectRatio="none">
    <polygon points="0,0 456,0 446,15 0,15" fill="#1a75bb"/>
    <polygon points="490,0 933,0 933,15 456,15" fill="#808285"/>
  </svg>
</section>

<section class="envelope envelope--back" aria-label="Envelope back">
  <svg class="flap" viewBox="0 0 933 132">
    <path d="M0,0 H933 L900,118 Q896,130 881,130 H52 Q37,130 33,118 Z" fill="#1a75bb"/>
  </svg>
  <div class="brand brand--flap"><span class="brand__mark"></span>TOVRIN</div>
  <div class="ghost-mark ghost-mark--back"></div>
</section>

</body>
</html>
```